Hi,

I would like to have a invitation made for a party. exactly like the picture in the link below.

http://pinboardia.example/pin/730215948361027459/

However, Please change the colors into fun/ girly feeling. font can be different and size of the card should be the same

Name of the girl: RINA
What: Bachelorette Party
Where:TOLO Boat
Dubai Coral Quay Sailing Club
When:7th of February 2013

No RSVP required. (so no need to put it)

```html
<!DOCTYPE html>
<html lang="en">
<head>
<meta charset="utf-8">
<title>Rina's Bachelorette Party Invitation</title>
<link rel="stylesheet" href="https://fonts.googleapis.com/css2?family=Rye&family=Sancreek&family=Oswald:wght@300;500&display=swap">
<style>
  :root {
    --paper: #ffffff;
    --ink-plum: #7a4a78;
    --ink-pink: #ec4c8e;
    --ink-orchid: #c46fd0;
    --ornament: #e9b9cc;
    --rule: #b98aa8;
  }
  html, body {
    margin: 0;
    padding: 0;
    overflow: hidden;
    background: var(--paper);
  }
  .invitation {
    position: relative;
    width: 1200px;
    height: 550px;
    background: var(--paper);
    overflow: hidden;
  }
  .ornament {
    position: absolute;
    background: var(--ornament);
    border-radius: 40% 40% 45% 45%;
  }
  .ornament--corner { width: 60px; height: 60px; }
  .ornament--tl { left: 12px;  top: 14px; }
  .ornament--tm { left: 334px; top: 14px; }
  .ornament--tr { left: 736px; top: 14px; }
  .ornament--bl { left: 12px;  top: 474px; }
  .ornament--bm { left: 334px; top: 474px; }
  .ornament--br { left: 736px; top: 474px; }
  .ornament--crest  { left: 488px; top: 78px;  width: 218px; height: 96px; border-radius: 50% 50% 30% 30%; }
  .ornament--footer { left: 488px; top: 482px; width: 218px; height: 50px; border-radius: 50%; }
  .ornament--panel  { left: 896px; top: 482px; width: 204px; height: 26px; border-radius: 50%; }

  .divider {
    position: absolute;
    width: 1px;
    height: 14px;
    background: var(--rule);
  }
  .divider--a-top { left: 405px; top: 16px; }
  .divider--a-bot { left: 405px; top: 520px; }
  .divider--b-top { left: 815px; top: 16px; }
  .divider--b-bot { left: 815px; top: 520px; }

  .headline {
    position: absolute;
    left: 0;
    top: 0;
    width: 818px;
    height: 550px;
  }
  .headline__name   { font-family: "Rye", serif; font-size: 56px; fill: var(--paper); }
  .headline__line   { font-family: "Rye", serif; font-size: 50px; fill: var(--ink-plum); }
  .headline__single { font-family: "Sancreek", serif; font-size: 215px; fill: var(--ink-pink); }

  .details {
    position: absolute;
    left: 837px;
    width: 356px;
    top: 0;
    height: 550px;
    font-family: "Oswald", sans-serif;
    font-weight: 300;
    text-transform: uppercase;
    color: var(--ink-plum);
  }
  .details > * {
    position: absolute;
    left: 0;
    width: 100%;
    margin: 0;
    text-align: center;
    line-height: 1;
    font-size: 16px;
  }
  .details__title { top: 110px; font-size: 20px; font-weight: 500; color: var(--ink-orchid); }
  .details__label { font-weight: 500; }
  .details__at    { top: 182px; }
  .details__venue { top: 224px; }
  .details__club  { top: 268px; }
  .details__on    { top: 312px; }
  .details__date  { top: 354px; }
</style>
</head>
<body>
<main class="invitation">
  <div class="ornament ornament--corner ornament--tl" role="img" aria-label="Filigree corner flourish"></div>
  <div class="ornament ornament--corner ornament--tm" role="img" aria-label="Filigree corner flourish"></div>
  <div class="ornament ornament--corner ornament--tr" role="img" aria-label="Filigree corner flourish"></div>
  <div class="ornament ornament--corner ornament--bl" role="img" aria-label="Filigree corner flourish"></div>
  <div class="ornament ornament--corner ornament--bm" role="img" aria-label="Filigree corner flourish"></div>
  <div class="ornament ornament--corner ornament--br" role="img" aria-label="Filigree corner flourish"></div>
  <div class="ornament ornament--crest" role="img" aria-label="Scrollwork crest"></div>
  <div class="ornament ornament--footer" role="img" aria-label="Scrollwork divider"></div>
  <div class="ornament ornament--panel" role="img" aria-label="Scrollwork divider"></div>

  <span class="divider divider--a-top"></span>
  <span class="divider divider--a-bot"></span>
  <span class="divider divider--b-top"></span>
  <span class="divider divider--b-bot"></span>

  <svg class="headline" viewBox="0 0 818 550" role="heading" aria-level="1" aria-label="Rina's last chance to celebrate being single">
    <defs>
      <filter id="emboss" x="-10%" y="-20%" width="130%" height="160%">
        <feDropShadow dx="5" dy="6" stdDeviation="4" flood-color="#8a6d85" flood-opacity="0.75"/>
      </filter>
      <filter id="lift" x="-5%" y="-10%" width="115%" height="130%">
        <feDropShadow dx="7" dy="9" stdDeviation="6" flood-color="#5a3050" flood-opacity="0.35"/>
      </filter>
    </defs>
    <text class="headline__name" x="78" y="172" textLength="289" lengthAdjust="spacingAndGlyphs" filter="url(#emboss)">RINA'S</text>
    <text class="headline__line" x="35" y="252" textLength="346" lengthAdjust="spacingAndGlyphs">LAST CHANCE TO</text>
    <text class="headline__line" x="423" y="252" textLength="367" lengthAdjust="spacingAndGlyphs">CELEBRATE BEING</text>
    <text class="headline__single" x="28" y="450" textLength="780" lengthAdjust="spacingAndGlyphs" filter="url(#lift)">SINGLE</text>
  </svg>

  <section class="details">
    <h2 class="details__title">Bachelorette Party</h2>
    <p class="details__label details__at">At</p>
    <p class="details__venue">TOLO Boat</p>
    <p class="details__club">Dubai Coral Quay Sailing Club</p>
    <p class="details__label details__on">On</p>
    <p class="details__date">7th of February 2013</p>
  </section>
</main>
</body>
</html>
```